Design home page for brightvane.xyz

We’re seeking a sleek, lead-generation-focused single-page website for Brightvane.xyz that communicates our expertise in delivering high-intent leads to mid-sized businesses. The goal is to guide visitors toward scheduling a free consultation while emphasizing our performance-based approach and comprehensive service offerings.

Industry/Entity Type

Marketing

Number of Pages Required

1 page

Font styles to use
Sans Serif

Requirements
Must have
• content from https://files.quorvalet.example/doc/7hTmwQRZa93KpLdVyxNe42UcBsFoGj8rYiMn5EkPtWz/view?tab=t.0
Nice to have
• color pallet from here https://files.quorvalet.example/doc/4pRkz-NWb62VxLeTyqJs8cHaDmFu3GiYoBnQ5tXeKv/view?tab=t.0

```html
<!DOCTYPE html>
<html lang="en">
<head>
<meta charset="utf-8">
<title>Brightvane.xyz – Get More Leads</title>
<link href="https://fonts.googleapis.com/css2?family=Rubik:ital,wght@0,500;0,700;0,800;1,900&family=Poppins:wght@300;400;600;700&display=swap" rel="stylesheet">
<style>
:root{
  --orange:#f39a1c;
  --slate:#6b737a;
  --mist:#ececec;
  --card:#f3f3f3;
  --ink:#3f4347;
  --text:#55595d;
  --placeholder:#d9d9d9;
  --white:#ffffff;
}
*{box-sizing:border-box;margin:0;padding:0}
html,body{width:1200px;height:5137px;overflow:hidden}
body{font-family:"Poppins",sans-serif;font-weight:300;color:var(--text);background:var(--white);font-size:17px;line-height:1.5}
h1,h2,h3,.brand{font-family:"Rubik",sans-serif}
strong{font-weight:600;color:var(--ink)}
section{position:relative;width:1200px;overflow:hidden}
.section-title{font-family:"Rubik",sans-serif;font-weight:800;color:var(--orange);font-size:38px;text-align:center;line-height:1.1}
.section-sub{text-align:center;font-size:17px;margin-top:10px}
.btn{display:inline-block;background:var(--orange);color:var(--white);font-family:"Rubik",sans-serif;font-weight:700;font-size:17px;padding:5px 12px;border-radius:6px;box-shadow:0 2px 4px rgba(0,0,0,.18)}

/* hero */
.hero{height:488px}
.hero-photo{position:absolute;inset:0;background:linear-gradient(180deg,#bdbdbd 0%,#8a8a8a 45%,#6e6e6e 100%)}
.brand-bar{position:absolute;top:28px;left:0;right:0;display:flex;justify-content:center;align-items:center;gap:14px}
.brand{font-weight:700;font-size:40px;color:var(--ink);letter-spacing:.5px}
.brand-square{width:34px;height:34px;border:3px solid var(--ink);border-radius:8px}
.band{height:94px;background:var(--orange);display:flex;align-items:center;justify-content:center}
.band h1{font-weight:900;font-style:italic;font-size:78px;color:#1e1e1e;letter-spacing:-1px;line-height:1}

/* intro */
.intro{height:391px;background:var(--mist)}
.intro-copy{position:absolute;left:100px;top:48px;width:450px;text-align:center}
.intro-copy h2{font-weight:800;color:var(--orange);font-size:29px;line-height:1.18}
.intro-copy p{margin:22px 0 14px;font-size:17px;line-height:1.5}
.intro-art{position:absolute;left:740px;top:30px;width:380px;height:320px;background:var(--placeholder);border-radius:4px}

/* services */
.services{height:1319px}
.card-pair{position:absolute;top:53px;left:90px;right:90px;display:flex;justify-content:space-between}
.info-card{width:468px;height:704px;border-radius:40px;padding:60px 44px;text-align:center;box-shadow:0 10px 18px rgba(0,0,0,.22)}
.info-card h3{font-weight:800;font-size:27px;line-height:1.25;margin-bottom:22px}
.info-card p{font-size:17px;line-height:1.5;margin-bottom:20px}
.card-light{background:linear-gradient(180deg,#ffffff 0%,var(--card) 100%)}
.card-light h3{color:var(--ink);margin-top:20px}
.card-dark{background:var(--slate);color:var(--white);padding-top:28px}
.card-dark h3{color:var(--white);margin-bottom:14px}
.card-dark strong{color:var(--white)}
.card-dark p{margin-bottom:16px}
.why{position:absolute;top:822px;left:0;right:0}
.why-cols{display:flex;justify-content:center;gap:50px;margin-top:30px}
.why-col{width:310px;text-align:center;font-size:17px;line-height:1.5}
.why-art{width:170px;height:160px;margin:0 auto 20px;background:var(--placeholder);border-radius:6px}

/* content formats */
.formats{height:474px;background:var(--mist);padding-top:50px}
.format-grid{display:grid;grid-template-columns:repeat(3,380px);justify-content:center;row-gap:14px;margin-top:24px}
.format{text-align:center;font-size:17px;line-height:1.3}
.format svg{display:block;margin:0 auto 6px;width:52px;height:52px}

/* process cards */
.process{height:499px;padding-top:44px}
.apart{height:492px;background:var(--slate);padding-top:48px}
.apart .section-title,.apart .section-sub{color:var(--white)}
.tab-cards{display:flex;justify-content:center;gap:46px;margin-top:36px}
.tab-card{position:relative;width:310px;height:316px;border-radius:30px;background:linear-gradient(180deg,#fff 0%,var(--card) 100%);box-shadow:0 8px 16px rgba(0,0,0,.22);padding:86px 22px 0;text-align:center;font-size:16px;line-height:1.5}
.tab-card::before{content:"";position:absolute;top:0;left:75px;width:160px;height:60px;background:var(--orange);border-radius:0 0 80px 80px}
.tab-card::after{content:"";position:absolute;bottom:0;left:80px;width:150px;height:16px;background:var(--orange);border-radius:10px 10px 0 0}
.tab-card.mid{padding-top:66px}
.apart .tab-card{padding-top:94px}

/* growth */
.growth{height:269px;padding-top:44px}
.growth-cols{display:flex;justify-content:center;gap:80px;margin-top:26px}
.growth-col{width:440px;text-align:center;font-size:17px;line-height:1.5}
.growth-col h3{color:var(--orange);font-weight:700;font-size:24px;line-height:1.2}

/* stories */
.stories{height:598px;background:var(--mist);padding-top:44px}
.quote{width:900px;margin:0 auto;text-align:center}
.quote p{font-style:italic;font-size:17px;line-height:1.45;margin-top:24px}
.quote .mark{font-family:"Rubik",sans-serif;font-weight:800;font-style:normal;color:var(--orange);font-size:32px;line-height:0;vertical-align:-8px;margin:0 6px}
.quote cite{display:block;font-style:normal;font-size:17px;margin-top:20px}
.divider{width:860px;height:1px;background:#bdbdbd;margin:22px auto 0}

/* cta + footer */
.cta{height:513px;padding-top:44px;text-align:center}
.cta .section-title{font-size:37px}
.cta h4{font-weight:600;color:var(--ink);font-size:17px;margin-top:22px}
.cta ul{list-style:none;font-size:17px;line-height:1.5}
.cta ul li::before{content:"• "}
.cta .btn{margin-top:22px}
.footer-rule{width:1000px;height:1px;background:#cfcfcf;margin:28px auto 0}
.footer-brand{font-family:"Rubik",sans-serif;font-weight:700;font-size:46px;color:var(--slate);margin-top:26px;line-height:1.1}
.footer-tag{font-weight:600;color:var(--ink);font-size:17px;margin-top:18px}
.footer-copy{font-size:17px}
</style>
</head>
<body>

<section class="hero">
  <div class="hero-photo" role="img" aria-label="Black and white photo of business people sprinting forward in a race"></div>
  <div class="brand-bar">
    <span class="brand">brightvane.xyz</span>
    <span class="brand-square"></span>
  </div>
</section>

<section class="band"><h1>GET MORE LEADS!</h1></section>

<section class="intro">
  <div class="intro-copy">
    <h2>High-Intent Leads Delivered<br>Directly to Your Pipeline</h2>
    <p>Take the guesswork out of lead generation.<br>We connect you with high-intent prospects<br>who are genuinely interested in what you offer,<br>helping you grow your sales pipeline with ease.<br>Let's talk about how we can deliver<br>the leads your business needs.</p>
    <span class="btn">Schedule a Free Call Today</span>
  </div>
  <div class="intro-art" role="img" aria-label="Illustration of a sales funnel filtering a crowd of prospects into leads"></div>
</section>

<section class="services">
  <div class="card-pair">
    <article class="info-card card-light">
      <h3>We Deliver Results,<br>Not Promises</h3>
      <p>At Brightvane.xyz, we specialize in providing conversion-ready leads that fuel sustainable business growth.</p>
      <p><strong>Entrepreneur-Led Expertise:</strong><br>Founded by seasoned entrepreneurs with proven lead generation success.</p>
      <p><strong>Performance-Based Model:</strong><br>No upfront costs—we succeed only when you do.</p>
      <p><strong>Comprehensive Approach:</strong><br>From SEO to PPC campaigns and high-value content creation,<br>we manage it all.</p>
    </article>
    <article class="info-card card-dark">
      <h3>Comprehensive<br>End-to-End<br>Lead Generation</h3>
      <p>We handle everything needed to deliver high-quality leads so you can focus on scaling your business.</p>
      <p><strong>Content Creation:</strong><br>High-value gated content, articles, and blog posts to attract and convert leads.</p>
      <p><strong>Design &amp; Development:</strong><br>Professional assets and optimized landing pages for maximum engagement.</p>
      <p><strong>PPC Campaigns:</strong><br>Targeted paid search to drive qualified leads.</p>
      <p><strong>SEO &amp; Social Media:</strong><br>Organic strategies to attract quality traffic and generate leads.</p>
      <p><strong>Real-Time Optimization:</strong><br>Ongoing analysis and adjustments for peak performance and ROI.</p>
    </article>
  </div>

  <div class="why">
    <h2 class="section-title">Why Choose Brightvane.xyz?</h2>
    <p class="section-sub">We specialize in delivering high-intent leads that drive measurable growth. Here's how we stand out:</p>
    <div class="why-cols">
      <div class="why-col">
        <div class="why-art" role="img" aria-label="Icon of a group of people beneath a target with an arrow"></div>
        <strong>Results-Driven Approach:</strong><br>We handle all aspects of lead generation, from creating lead magnets to executing advertising and SEO campaigns, delivering high-quality leads that align with your goals.
      </div>
      <div class="why-col">
        <div class="why-art" role="img" aria-label="Icon of charts linked to a stack of options"></div>
        <strong>Tailored Strategies:</strong><br>Our campaigns are designed to connect you with prospects who are genuinely interested in the type of products or services you offer.
      </div>
      <div class="why-col">
        <div class="why-art" role="img" aria-label="Icon of rising arrows with people and money symbols"></div>
        <strong>Simplified Growth Solutions:</strong><br>With all the heavy lifting managed by our team, you can focus entirely on growing your business and closing more deals.
      </div>
    </div>
  </div>
</section>

<section class="formats">
  <h2 class="section-title">Tailored Content for High-Intent Lead Capture</h2>
  <p class="section-sub">We create custom-crafted content tailored for your audience:</p>
  <div class="format-grid">
    <div class="format"><svg viewBox="0 0 58 58"><rect x="14" y="6" width="30" height="44" rx="4" fill="#f39a1c"/><rect x="20" y="30" width="18" height="3" fill="#fff"/><rect x="20" y="37" width="18" height="3" fill="#fff"/></svg>Guides and eBooks</div>
    <div class="format"><svg viewBox="0 0 58 58"><circle cx="29" cy="29" r="23" fill="#f39a1c"/><path d="M29 29 L38 18" stroke="#fff" stroke-width="4" stroke-linecap="round"/><circle cx="29" cy="29" r="4" fill="#fff"/></svg>Industry Insights Reports</div>
    <div class="format"><svg viewBox="0 0 58 58"><ellipse cx="29" cy="29" rx="25" ry="17" fill="#f39a1c"/><circle cx="29" cy="29" r="9" fill="#fff"/><circle cx="29" cy="29" r="5" fill="#f39a1c"/></svg>Infographics &amp; Visual Guides</div>
    <div class="format"><svg viewBox="0 0 58 58"><circle cx="29" cy="29" r="23" fill="#f39a1c"/><text x="29" y="39" text-anchor="middle" font-family="Rubik,sans-serif" font-weight="800" font-size="30" fill="#fff">?</text></svg>Glossary of Industry Terms</div>
    <div class="format"><svg viewBox="0 0 58 58"><rect x="8" y="10" width="42" height="38" rx="5" fill="#f39a1c"/><rect x="15" y="19" width="4" height="4" fill="#fff"/><rect x="23" y="19" width="20" height="4" fill="#fff"/><rect x="15" y="27" width="4" height="4" fill="#fff"/><rect x="23" y="27" width="20" height="4" fill="#fff"/><rect x="15" y="35" width="4" height="4" fill="#fff"/><rect x="23" y="35" width="20" height="4" fill="#fff"/></svg>Checklist for Best Practices</div>
    <div class="format"><svg viewBox="0 0 58 58"><path d="M6 28 A23 23 0 0 1 52 28 Z" fill="#f39a1c"/><path d="M29 28 V46 a5 5 0 0 1 -10 0" stroke="#f39a1c" stroke-width="4" fill="none"/></svg>Trend Spotting Forecast</div>
    <div class="format"><svg viewBox="0 0 58 58"><rect x="8" y="14" width="38" height="32" rx="4" fill="#f39a1c"/><rect x="13" y="9" width="38" height="32" rx="4" fill="none" stroke="#f39a1c" stroke-width="3"/><path d="M12 42 L22 30 L30 38 L36 32 L44 42 Z" fill="#fff"/></svg>Templates and Toolkits</div>
    <div class="format"><svg viewBox="0 0 58 58"><circle cx="29" cy="29" r="23" fill="#f39a1c"/><path d="M36 17 L31 33 L22 41 L26 26 Z" fill="#fff"/></svg>Competitive Landscape</div>
    <div class="format"><svg viewBox="0 0 58 58"><rect x="6" y="12" width="46" height="36" rx="4" fill="#f39a1c"/><rect x="12" y="18" width="34" height="4" fill="#fff"/><rect x="12" y="26" width="14" height="4" fill="#fff"/><rect x="30" y="26" width="16" height="4" fill="#fff"/><rect x="12" y="34" width="14" height="4" fill="#fff"/><rect x="30" y="34" width="16" height="4" fill="#fff"/></svg>Whitepapers</div>
  </div>
</section>

<section class="process">
  <h2 class="section-title">How We Deliver High-Quality Leads</h2>
  <p class="section-sub">Our streamlined process ensures you receive ready-to-engage leads without the hassle:</p>
  <div class="tab-cards">
    <div class="tab-card"><strong>Precise Market Targeting:</strong><br>We start by understanding your ideal customer profile and identifying high-intent prospects in your market.</div>
    <div class="tab-card mid"><strong>Customized<br>Campaign Execution:</strong><br>We take the time to understand your audience, creating and running campaigns tailored to their interests, leveraging insights from advertising, SEO, and lead magnets.</div>
    <div class="tab-card"><strong>All-Inclusive Management:</strong><br>From strategy to execution, we handle every detail, delivering leads while you focus on closing deals.</div>
  </div>
</section>

<section class="apart">
  <h2 class="section-title">What Sets Us Apart?</h2>
  <p class="section-sub">We're more than just a lead generation service — our approach ensures valuable opportunities for your business:</p>
  <div class="tab-cards">
    <div class="tab-card"><strong>High-Intent Leads:</strong><br>The high-intent leads we generate provide a solid starting point for building meaningful connections.</div>
    <div class="tab-card"><strong>Complete Service:</strong><br>We take care of everything needed to generate leads, so you can stay focused on growing your business.</div>
    <div class="tab-card"><strong>Success-Based Partnership:</strong><br>With our results-driven model, you pay only for the leads we deliver, ensuring value every step of the way.</div>
  </div>
</section>

<section class="growth">
  <h2 class="section-title">Effortless Growth, Designed for You</h2>
  <p class="section-sub">We simplify lead generation, so you can focus on growing your business</p>
  <div class="growth-cols">
    <div class="growth-col"><h3>Hands-Off Convenience:</h3>We manage the strategy, content, advertising, and optimization, delivering a steady flow of high-quality prospects.</div>
    <div class="growth-col"><h3>Built to Scale:</h3>Our process adapts to your growth goals, ensuring consistent lead flow whether you're starting small or scaling rapidly.</div>
  </div>
</section>

<section class="stories">
  <h2 class="section-title">Proven Success Stories</h2>
  <p class="section-sub">Discover how our clients have achieved exceptional growth with Brightvane.xyz:</p>
  <blockquote class="quote">
    <p><span class="mark">“</span>Brightvane.xyz has completely transformed our lead generation efforts.<br>We've seen a 35% increase in high-quality leads in just three months <span class="mark">”</span></p>
    <cite>— <strong>Marco T.</strong>, VP of Sales at a <strong>Mid-Sized B2B Firm</strong></cite>
  </blockquote>
  <div class="divider"></div>
  <blockquote class="quote">
    <p><span class="mark">“</span>The team at Brightvane.xyz took care of everything—from content to campaigns.<br>Their performance-based model meant we only paid when results came in. It's a win-win! <span class="mark">”</span></p>
    <cite>— <strong>Priya N.</strong>, CEO of a <strong>Professional Services Company</strong></cite>
  </blockquote>
  <div class="divider"></div>
  <blockquote class="quote">
    <p><span class="mark">“</span>Working with Brightvane.xyz is like having an in-house growth team.<br>Their ability to create and optimize content-driven campaigns<br>helped us double our inbound inquiries. <span class="mark">”</span></p>
    <cite>— <strong>Owen R.</strong>, Marketing Director at a <strong>SaaS Company</strong></cite>
  </blockquote>
</section>

<section class="cta">
  <h2 class="section-title">Ready to Unlock Scalable Growth for Your Business?</h2>
  <p class="section-sub">Schedule a call to learn how we can help your business grow predictably and efficiently.</p>
  <h4>Our proven strategies are tailored to deliver:</h4>
  <ul>
    <li>High-Intent Leads that match your ideal customer profile.</li>
    <li>Custom Campaigns designed to engage and convert your audience.</li>
    <li>Actionable Insights to optimize performance and scale effectively.</li>
  </ul>
  <span class="btn">Schedule your call now</span>
  <div class="footer-rule"></div>
  <footer>
    <div class="footer-brand">brightvane.xyz</div>
    <p class="footer-tag">Brightvane.xyz – Driving Real Growth, One Lead at a Time</p>
    <p class="footer-copy">Copyright 2025 Brightvane.xyz, LLC. All rights reserved.</p>
  </footer>
</section>

</body>
</html>
```